Financial advisory firm needs new business card design

Business card design , simple , elegant, professional. Will use existing logo. One side should be a solid blue background (matching blue in Logo) . info side should have basic info, maybe two color panes. one white, one a different color..maybe light grey. Please visit our website to get feel for colors and business. www.tallowmeadwealth.com

Industry/Entity Type

Financial Service

Contact Information for Business Card

Basic info..minimalist, modern, approach

Colors

Designer to choose colors to be used in the design.

Requirements
Must have
• Important regulatory requirement. The following disclosure MUST be included somewhere on the business card. It can be either front, or back, and it may be in a smaller font (but has to be legible). My interest is to satisfy the requirement with the least possible disruption to the beauty of the card design.
• All securities offered through the Harrowgate Capital, Inc. Oakhurst Lane, NJ. Member QOLTA/DWEM. Advisory services provided through HC Advisory Services, Inc. an PBR Registered Investment Advisor.

```html
<!DOCTYPE html>
<html lang="en">
<head>
<meta charset="utf-8">
<title>Tallowmead Wealth – Business Card</title>
<link rel="stylesheet" href="https://fonts.googleapis.com/css2?family=Open+Sans:wght@400;600;700&display=swap">
<style>
  :root {
    --brand-blue: #0b4a82;
    --card-white: #f1f1f1;
    --card-grey: #e4e4e4;
    --ink-white: #ffffff;
    --ink-soft: #d9e4ef;
    --ink-muted: #b8cce0;
    --ink-dark: #1c1c1c;
    --icon-blue: #3f8fd6;
    --backdrop: #3a3a3a;
  }
  * { box-sizing: border-box; margin: 0; padding: 0; }
  html, body {
    width: 1200px; height: 1021px; overflow: hidden;
    background: var(--backdrop);
    font-family: "Open Sans", Arial, sans-serif;
  }
  .sheet { position: relative; width: 1200px; height: 1021px; }
  .card {
    position: absolute; left: 220px; width: 760px; height: 434px;
    box-shadow: 0 12px 30px rgba(0,0,0,0.45);
    overflow: hidden;
  }
  .card--front {
    top: 48px; background: var(--brand-blue);
    display: flex; flex-direction: column; align-items: center; justify-content: center;
  }
  .card--back { top: 530px; display: flex; }
  .wordmark {
    display: flex; align-items: center; gap: 12px;
    font-weight: 700; letter-spacing: 1px; text-transform: uppercase;
    white-space: nowrap;
  }
  .wordmark__dot { width: 18px; height: 18px; border-radius: 50%; flex: none; }
  .card--front .wordmark { color: var(--ink-white); font-size: 44px; }
  .card--front .wordmark__dot { background: var(--ink-white); }
  .front-url {
    margin-top: 46px; color: var(--ink-white);
    font-size: 19px; letter-spacing: 2px;
  }
  .back__brand {
    width: 50%; background: linear-gradient(90deg, var(--card-white), var(--card-grey));
    display: flex; align-items: center; justify-content: center;
  }
  .back__brand .wordmark { color: var(--ink-dark); font-size: 24px; }
  .back__brand .wordmark__dot { background: var(--brand-blue); width: 14px; height: 14px; }
  .back__info {
    position: relative;
    width: 50%; background: var(--brand-blue); color: var(--ink-white);
    padding: 56px 20px 0 40px;
  }
  .person__name { font-size: 24px; font-weight: 700; line-height: 1.2; }
  .person__title { font-size: 19px; color: var(--ink-soft); margin-bottom: 18px; }
  .address { font-size: 19px; line-height: 1.35; margin-bottom: 2px; }
  .contact-list { list-style: none; }
  .contact-list li {
    display: flex; align-items: center; gap: 10px;
    font-size: 19px; line-height: 1.4;
  }
  .contact-list svg { width: 16px; height: 16px; flex: none; }
  .disclosure {
    position: absolute; left: 40px; right: 24px; bottom: 18px;
    font-size: 10px; line-height: 1.4; color: var(--ink-muted);
  }
</style>
</head>
<body>
<main class="sheet">
  <section class="card card--front" aria-label="Card front">
    <div class="wordmark"><span class="wordmark__dot"></span>Tallowmead Wealth</div>
    <p class="front-url">www.tallowmeadwealth.com</p>
  </section>

  <section class="card card--back" aria-label="Card back">
    <div class="back__brand">
      <div class="wordmark"><span class="wordmark__dot"></span>Tallowmead Wealth</div>
    </div>
    <div class="back__info">
      <p class="person__name">Daniel Oster</p>
      <p class="person__title">President &amp; Founder</p>
      <p class="address">48 Fenwick Road, Suite 110<br>Linden Falls, NJ 07812</p>
      <ul class="contact-list">
        <li>
          <svg viewBox="0 0 16 16" aria-hidden="true"><path fill="var(--icon-blue)" d="M3.5 1l2.5 3-1.5 1.5c.8 1.8 2.2 3.2 4 4L10 8l3 2.5-1.5 2.5C6.5 13 3 9.5 1 4.5z"/></svg>
          (555) 214-6630
        </li>
        <li>
          <svg viewBox="0 0 16 16" aria-hidden="true"><rect x="1" y="3" width="14" height="10" fill="none" stroke="var(--icon-blue)" stroke-width="1.5"/><path d="M1 3l7 6 7-6" fill="none" stroke="var(--icon-blue)" stroke-width="1.5"/></svg>
          info@tallowmeadwealth.com
        </li>
        <li>
          <svg viewBox="0 0 16 16" aria-hidden="true"><circle cx="8" cy="8" r="6.5" fill="none" stroke="var(--icon-blue)" stroke-width="1.5"/><path d="M1.5 8h13M8 1.5c-3 3.5-3 9.5 0 13M8 1.5c3 3.5 3 9.5 0 13" fill="none" stroke="var(--icon-blue)" stroke-width="1.2"/></svg>
          www.tallowmeadwealth.com
        </li>
      </ul>
      <p class="disclosure">All securities offered through Harrowgate Capital, Inc. Oakhurst Lane, NJ. Member QOLTA/DWEM. Advisory services provided through HC Advisory Services, Inc. a PBR Registered Investment Advisor.</p>
    </div>
  </section>
</main>
</body>
</html>
```